A book cover for an ESL self-study guide to English small talk with exercises and answers

I need a book cover for an ESL self-study guide to English small talk with exercises. It has useful phrases, idioms, and vocabulary in it but I will provide the blub for the back of the book. I would like a simple design. I had the idea to use a red background and the letters 'English' being large across the front in Union Jack lettering then 'ESL' below in different lettering and Small talk further down. I am not sure if the Union Jack lettering will stand out well enough on a red background so we might have to use a different background or edging for those letters but Ideally, I'd like the book to be red and either the 'ESL' or 'Small Talk' to be a vivid blue but again if something else looks better go with it. If it looks like this design idea doesn't work I am open to other ideas too. If the Union Jack lettering is not used I will need a Union Jack on there somewhere to show that the book is in British English. Those are my ideas but ultimately, you guys are the professionals.

Target Market(s)

People who are learning English from ESL students to professionals. I expect the market to be more professionals.

Industry/Entity Type

Education.

Colors
EB3D1F
EC4F4E
F09395
F8D3D4
FCEDEE

Requirements
Must have
• A Union Jack or union jack lettering to show the book is in British English. I would like to cover to be striking and stand out from the others in it's genre without being gaudy.
Nice to have
• I would like the cover to be red but ultimately you guys are the professionals and I'm sure you know more than I do. Scripts should be easy to read as it's for ESL students.

```html
<!DOCTYPE html>
<html lang="en">
<head>
<meta charset="utf-8">
<title>Chatter EFL Daily Chats – Book Cover</title>
<link rel="stylesheet" href="https://fonts.googleapis.com/css2?family=Bebas+Neue&family=Tinos:wght@400;700&family=Lexend:wght@700&display=swap">
<style>
  :root {
    --cover-red: #d42027;
    --royal-blue: #2b3990;
    --flag-navy: #232d7a;
    --flag-red: #c8202a;
    --flag-white: #f1f1f4;
    --paper-white: #ffffff;
    --ink-black: #111111;
  }
  * { margin: 0; padding: 0; box-sizing: border-box; }
  html, body {
    width: 1200px; height: 858px; overflow: hidden;
    background: var(--cover-red);
  }
  .cover {
    position: relative; width: 1200px; height: 858px;
    background: var(--cover-red); overflow: hidden;
  }
  .flag-banner {
    position: absolute; left: 0; top: 0; width: 1200px; height: 250px;
  }
  .back-blurb {
    position: absolute; left: 86px; top: 270px; width: 400px;
    font-family: "Tinos", "Times New Roman", serif;
    font-size: 12.6px; line-height: 15.4px; color: var(--paper-white);
  }
  .back-blurb p { margin-bottom: 15.4px; }
  .back-blurb strong { font-weight: 700; }

  .spine {
    position: absolute; left: 582px; top: 254px; width: 36px; height: 450px;
  }
  .spine-title {
    position: absolute; left: 0; top: 0; width: 36px; height: 116px;
  }
  .spine-badge {
    position: absolute; left: 0; top: 150px; width: 36px; height: 106px;
    background: var(--royal-blue);
    writing-mode: vertical-rl;
    display: flex; align-items: center; justify-content: center;
    font-family: "Tinos", "Times New Roman", serif; font-weight: 700;
    font-size: 19px; letter-spacing: 8px; color: var(--paper-white);
  }
  .spine-subtitle {
    position: absolute; left: 4px; top: 296px; width: 28px; height: 148px;
  }

  .front-title {
    position: absolute; left: 700px; top: 262px; width: 424px; height: 150px;
  }
  .front-badge {
    position: absolute; left: 790px; top: 429px; width: 240px; height: 78px;
    background: var(--royal-blue);
    display: flex; align-items: center; justify-content: center;
    font-family: "Tinos", "Times New Roman", serif; font-weight: 700;
    font-size: 54px; letter-spacing: 22px; padding-left: 22px;
    color: var(--paper-white);
  }
  .speech-bubble {
    position: absolute; left: 760px; top: 600px; width: 310px; height: 160px;
  }
</style>
</head>
<body>
<main class="cover">

  <svg class="flag-banner" viewBox="0 0 1200 250" role="img" aria-label="Draped Union Jack flag fabric across the top of the cover">
    <defs>
      <linearGradient id="flagTones" x1="0" y1="0" x2="1" y2="0">
        <stop offset="0" stop-color="var(--flag-navy)"/>
        <stop offset="0.18" stop-color="var(--flag-red)"/>
        <stop offset="0.32" stop-color="var(--flag-white)"/>
        <stop offset="0.5" stop-color="var(--flag-navy)"/>
        <stop offset="0.68" stop-color="var(--flag-white)"/>
        <stop offset="0.82" stop-color="var(--flag-red)"/>
        <stop offset="1" stop-color="var(--flag-navy)"/>
      </linearGradient>
    </defs>
    <path fill="url(#flagTones)"
      d="M0 0 H1200 V140 C1150 150 1100 190 1040 244 C980 220 900 200 840 190 C760 178 680 176 600 172 C520 176 440 178 360 190 C300 200 230 225 180 244 C120 190 60 150 0 138 Z"/>
  </svg>

  <section class="back-blurb">
    <p>Step into everyday British conversation with “Chatter EFL Daily Chats,” a practical handbook written by an experienced native-speaking British teacher who has coached learners online for many years.</p>
    <p>Easy, natural chatting is a skill anyone can <strong>practise</strong>, and this book works as a complete self-study course that guides you step by step towards relaxed, friendly British English conversation.</p>
    <p>It suits anyone who wants to speak more confidently in daily life. Inside you will find key words, handy phrases, collocations, phrasal verbs and common idioms grouped by familiar topics, all chosen to lift your everyday chatting skills.</p>
    <p>Whether you are learning for exams or want to sound more natural at work, this handbook gives you a clear, step-by-step plan with practice tasks and full answers that help new language stick.</p>
    <p>You will also get tips from native speakers for an honest picture of how people really talk, plus ready phrases for many different social moments, supported by online audio tracks so you can polish your pronunciation.</p>
    <p>Open the book and begin building easy, confident conversations today!</p>
  </section>

  <section class="spine">
    <svg class="spine-title" viewBox="0 0 36 116">
      <text transform="translate(2 0) rotate(90)" x="0" y="0" textLength="116" lengthAdjust="spacingAndGlyphs"
        font-family="Bebas Neue, Oswald, sans-serif" font-size="45" fill="var(--paper-white)">CHATTER</text>
    </svg>
    <div class="spine-badge">EFL</div>
    <svg class="spine-subtitle" viewBox="0 0 28 148">
      <text transform="translate(5 0) rotate(90)" x="0" y="0" textLength="148" lengthAdjust="spacingAndGlyphs"
        font-family="Lexend, Montserrat, sans-serif" font-weight="700" font-size="28" fill="var(--ink-black)">Daily Chats</text>
    </svg>
  </section>

  <svg class="front-title" viewBox="0 0 424 150">
    <text x="4" y="138" textLength="412" lengthAdjust="spacingAndGlyphs"
      font-family="Bebas Neue, Oswald, sans-serif" font-size="184" fill="var(--paper-white)">CHATTER</text>
  </svg>

  <div class="front-badge">EFL</div>

  <svg class="speech-bubble" viewBox="0 0 310 160">
    <path fill="var(--paper-white)"
      d="M150 8 C230 8 296 36 296 70 C296 96 264 118 222 126 C230 140 246 148 264 152 C236 152 212 144 196 132 C182 133 166 134 150 134 C70 134 4 106 4 70 C4 36 70 8 150 8 Z"/>
    <text x="32" y="88" textLength="236" lengthAdjust="spacingAndGlyphs"
      font-family="Lexend, Montserrat, sans-serif" font-weight="700" font-size="46"
      fill="var(--royal-blue)">Daily Chats</text>
  </svg>

</main>
</body>
</html>
```